Willowmere Therapy (Endure - Renew - Flourish) - Double Sided Business Card

I would like a 2-sided business card. Front: Matte Black or Navy with Logo & Tagline. Back: Name, Address, Phone Number, Email, & Website (maybe would like to include a small map pin-pointing location); Prefer front to be a gold/silver foil (iridescent); Back prefer white or light colored background with lettering that is easy to read and simple

Target Market(s)

Individuals & Couples (13 y.o. - ALL Adults); High end clientele

Industry/Entity Type

Licensed Professional Counselor (Mental Health)

Contact Information for Business Card

Name: Willowmere Therapy; Tagline: Endure - Renew - Flourish; Address: 3175 W. Calder Ave., Suite 842, Fort Worth, TX 76142; Phone: (214) 738-2956; Website: www.WillowmereTherapy.example

Font styles to use
Serif

Requirements
Must have
• Logo on Front (Large) prefer gold/silver foil on a matte dark color (i.e. black, navy, etc.); Back of Card: All other relevant information

```html
<!DOCTYPE html>
<html lang="en">
<head>
<meta charset="utf-8">
<title>Willowmere Therapy – Business Card</title>
<link href="https://fonts.googleapis.com/css2?family=Cinzel:wght@400;700&family=Tinos:wght@400&display=swap" rel="stylesheet">
<style>
  :root {
    --backdrop: #1d1d1f;
    --navy: #211d5a;
    --gold: #d4b45a;
    --paper: #ffffff;
    --ink: #3a3a3a;
    --rule: #8e8e93;
    --ghost: #f2f2f2;
  }
  * { box-sizing: border-box; margin: 0; padding: 0; }
  html, body {
    width: 1200px; height: 988px; overflow: hidden;
    background: var(--backdrop);
  }
  .stage {
    position: relative; width: 1200px; height: 988px;
  }
  .card {
    position: absolute; left: 320px; width: 560px; height: 320px;
    border-radius: 22px; overflow: hidden;
    box-shadow: 0 10px 30px rgba(0,0,0,.55);
  }
  .card--front { top: 150px; background: var(--navy); }
  .card--back  { top: 518px; background: var(--paper); }

  /* front */
  .front-mark {
    position: absolute; inset: 0;
    display: flex; flex-direction: column; align-items: center; justify-content: center;
  }
  .front-mark .dot {
    width: 70px; height: 70px; border-radius: 50%;
    border: 3px solid var(--gold); margin-bottom: 18px;
  }
  .brand-name {
    font-family: "Cinzel", serif; font-weight: 400; color: var(--gold);
    letter-spacing: 2px; line-height: 1.1; text-align: center;
  }
  .card--front .brand-name { font-size: 38px; }
  .tagline {
    font-family: "Cinzel", serif; color: var(--gold);
    letter-spacing: 1.5px; text-transform: uppercase;
  }
  .card--front .tagline {
    font-size: 14px; margin-top: 12px; padding-top: 10px;
    border-top: 2px solid #ffffff; width: 380px; text-align: center;
  }

  /* back */
  .ghost-disc {
    position: absolute; right: -60px; top: 30px;
    width: 300px; height: 300px; border-radius: 50%;
    background: var(--ghost);
  }
  .back-content { position: absolute; left: 38px; top: 34px; }
  .card--back .brand-name { font-size: 30px; text-align: left; }
  .card--back .tagline {
    font-size: 11.5px; margin-top: 6px; padding-top: 6px;
    border-top: 2px solid var(--rule); width: 330px;
  }
  .person-name {
    font-family: "Cinzel", serif; font-weight: 700; color: var(--gold);
    font-size: 22px; margin-top: 30px; letter-spacing: 1px;
  }
  .person-title, .address, .contact-list {
    font-family: "Tinos", serif; color: var(--ink); font-size: 15px; line-height: 1.3;
  }
  .address { margin-top: 10px; }
  .contact-list { list-style: none; margin-top: 10px; }
  .contact-list li { display: flex; align-items: center; gap: 8px; }
  .contact-list svg { width: 13px; height: 13px; fill: var(--gold); flex: none; }
</style>
</head>
<body>
<main class="stage">
  <section class="card card--front" aria-label="Card front">
    <div class="front-mark">
      <span class="dot"></span>
      <h1 class="brand-name">Willowmere Therapy</h1>
      <p class="tagline">Endure - Renew - Flourish</p>
    </div>
  </section>

  <section class="card card--back" aria-label="Card back">
    <div class="ghost-disc"></div>
    <div class="back-content">
      <h2 class="brand-name">Willowmere Therapy</h2>
      <p class="tagline">Endure - Renew - Flourish</p>
      <p class="person-name">DANIEL WHITLOCK</p>
      <p class="person-title">CEO/Founder</p>
      <p class="address">3175 W. Calder Ave., Suite 842<br>Fort Worth, TX 76142</p>
      <ul class="contact-list">
        <li><svg viewBox="0 0 24 24"><path d="M6.6 10.8a15.1 15.1 0 0 0 6.6 6.6l2.2-2.2a1 1 0 0 1 1-.25 11.4 11.4 0 0 0 3.6.57 1 1 0 0 1 1 1V20a1 1 0 0 1-1 1A17 17 0 0 1 3 4a1 1 0 0 1 1-1h3.5a1 1 0 0 1 1 1c0 1.25.2 2.46.57 3.6a1 1 0 0 1-.25 1z"/></svg>(214) 738-2956</li>
        <li><svg viewBox="0 0 24 24"><path d="M2 5h20v14H2z M2 5l10 8 10-8" stroke="#fff" stroke-width="1.5"/></svg>info@willowmeretherapy.example</li>
        <li><svg viewBox="0 0 24 24"><circle cx="12" cy="12" r="10"/><path d="M2 12h20M12 2c3 3 3 17 0 20M12 2c-3 3-3 17 0 20" stroke="#fff" stroke-width="1.3" fill="none"/></svg>www.WillowmereTherapy.example</li>
      </ul>
    </div>
  </section>
</main>
</body>
</html>
```